Business Card Design

I am an Event and Wedding Planner in need of an eye catching business card featuring my logo (attached), my contact details, and my company tagline (Making each one of your gatherings radiant...) I would like the tagline in font similar the logo's font.
Updates
I have just noticed that my logo has a misspelling so for the final design, I will be uploading a corrected logo as soon as I have it.
My apologies.
Reason: Waiting on a corrected logo...Occasions is misspelled and it should say Weddings not Wedding
The logo has been corrected so now Occasions is spelled correctly and it says Weddings instead of Wedding. Please use Edwardian Script ITC as the font for the tagline so it will match the logo. Thank you for your patience.
Target Market(s)
Engaged couples and people hosting milestone celebrations. 25-50 years old, predominately female
Industry/Entity Type
Business
Contact Information for Business Card
Delphine Marsh, Event Manager / Owner, Mobile: 0491 836 254, Email: delphine@radiantgatheringsco.com.au, www.radiantgatheringsco.com.au, Making each one of your gatherings radiant...

```html
<!DOCTYPE html>
<html lang="en">
<head>
<meta charset="utf-8">
<title>Radiant Gatherings Co. — Business Card</title>
<link rel="stylesheet" href="https://fonts.googleapis.com/css2?family=Pinyon+Script&family=Cormorant+Garamond:wght@500&display=swap">
<style>
  :root {
    --backdrop: #2b2b2d;
    --card-white: #fbfafa;
    --blush: #f1d9dc;
    --blush-line: #e6b4b9;
    --crimson: #c4232b;
    --ink: #1d1b1c;
    --photo-light: #e9ebe6;
    --photo-mid: #b9bcbc;
    --photo-bloom: #f3f2dc;
  }
  * { box-sizing: border-box; margin: 0; padding: 0; }
  html, body {
    width: 1200px; height: 900px; overflow: hidden;
    background: var(--backdrop);
  }
  .canvas {
    position: relative; width: 1200px; height: 900px;
  }
  .card {
    position: absolute; left: 280px; width: 640px; height: 366px;
    background: var(--card-white); overflow: hidden;
    box-shadow: 0 10px 30px rgba(0,0,0,.45);
  }
  .card--front { top: 58px; }
  .card--back { top: 476px; }

  /* Front */
  .tagline-band {
    position: absolute; left: 0; top: 0; width: 100%; height: 70px;
    background: var(--blush);
  }
  .tagline {
    position: absolute; right: 26px; top: 14px;
    font: 32px "Pinyon Script", cursive; color: var(--ink);
  }
  .brand {
    position: absolute; left: 32px; top: 98px;
    display: flex; align-items: center; gap: 10px;
  }
  .brand__name {
    font: 40px "Pinyon Script", cursive; color: var(--ink); line-height: 1;
  }
  .brand__dot {
    width: 14px; height: 14px; border-radius: 50%; background: var(--crimson);
  }
  .rule--blush {
    position: absolute; left: 0; top: 214px; width: 390px; height: 4px;
    background: var(--blush-line);
  }
  .rule--crimson {
    position: absolute; left: 420px; top: 232px; width: 220px; height: 6px;
    background: var(--crimson);
  }
  .contact {
    position: absolute; display: flex; align-items: center; gap: 12px;
    font: 500 17px "Cormorant Garamond", serif; color: var(--ink);
  }
  .contact--web { left: 32px; top: 180px; }
  .contact--phone { left: 430px; top: 248px; font-size: 19px; }
  .contact svg { flex: none; }
  .person {
    position: absolute; right: 34px; top: 150px; text-align: right;
  }
  .person__name {
    font: 38px "Pinyon Script", cursive; color: var(--ink); line-height: 1;
  }
  .person__role {
    font: 17px "Pinyon Script", cursive; color: var(--ink); margin-right: 40px;
  }
  .base-band {
    position: absolute; left: 0; bottom: 0; width: 100%; height: 82px;
    background: var(--crimson);
  }

  /* Back */
  .photo {
    position: absolute; left: 0; top: 0; width: 100%; height: 286px;
    background:
      radial-gradient(ellipse 240px 130px at 68% 88%, var(--photo-bloom), transparent 75%),
      linear-gradient(120deg, var(--photo-mid), var(--photo-light) 55%, #d8dad6);
  }
  .back-brand {
    position: absolute; right: 40px; top: 110px;
    display: flex; align-items: center; gap: 10px;
  }
  .back-brand .brand__name { font-size: 42px; }
  .email-band {
    position: absolute; left: 0; bottom: 0; width: 100%; height: 80px;
    background: var(--crimson);
    display: flex; align-items: center; padding-left: 40px;
  }
  .email {
    font: 500 28px "Cormorant Garamond", serif; color: #fff; letter-spacing: .2px;
  }
</style>
</head>
<body>
<main class="canvas">

  <section class="card card--front" aria-label="Business card front">
    <div class="tagline-band"></div>
    <p class="tagline">Making each one of your gatherings radiant...</p>

    <div class="brand">
      <span class="brand__name">Radiant Gatherings Co.</span>
      <span class="brand__dot"></span>
    </div>

    <p class="contact contact--web">
      <svg width="18" height="13" viewBox="0 0 18 13" aria-hidden="true">
        <rect x="0.5" y="0.5" width="17" height="12" fill="#1d1b1c"/>
        <path d="M1 1 L9 7 L17 1" fill="none" stroke="#fbfafa" stroke-width="1.2"/>
      </svg>
      www.radiantgatheringsco.com.au
    </p>
    <div class="rule--blush"></div>

    <div class="person">
      <p class="person__name">Delphine Marsh</p>
      <p class="person__role">Event Manager</p>
    </div>

    <div class="rule--crimson"></div>
    <p class="contact contact--phone">
      <svg width="10" height="16" viewBox="0 0 10 16" aria-hidden="true">
        <rect x="1" y="1" width="8" height="14" rx="1.5" fill="none" stroke="#1d1b1c" stroke-width="1.4"/>
        <line x1="3.5" y1="12.5" x2="6.5" y2="12.5" stroke="#1d1b1c" stroke-width="1.2"/>
      </svg>
      0491 836 254
    </p>

    <div class="base-band"></div>
  </section>

  <section class="card card--back" aria-label="Business card back">
    <div class="photo" role="img" aria-label="Photo of a bride's hand holding a bouquet of white roses and calla lilies tied with navy and silver ribbon against a white gown"></div>
    <div class="back-brand">
      <span class="brand__name">Radiant Gatherings Co.</span>
      <span class="brand__dot"></span>
    </div>
    <div class="email-band">
      <p class="email">delphine@radiantgatheringsco.com.au</p>
    </div>
  </section>

</main>
</body>
</html>
```